Kestrel Roofing & Restoration Business Card Design

Lookiing for a double sided business card design that will have rounded corners, will look good with Spot UV, Soft Laminate, or Gloss
Front of card should have Logo, Name and Contact Info, License numbers
Back of card should have Logo, maybe other small details

```html
<!DOCTYPE html>
<html lang="en">
<head>
<meta charset="utf-8">
<title>Kestrel Roofing &amp; Restoration — Business Cards</title>
<link href="https://fonts.googleapis.com/css2?family=Poppins:wght@300;400;600;700&display=swap" rel="stylesheet">
<style>
  :root{
    --page:#dcdcdc;
    --ink-dark:#232323;
    --ink-deep:#0b0b0b;
    --ink-mid:#2c2c2c;
    --sky:#4bbde8;
    --sky-pale:#cdebf6;
    --fold:#4a4a4a;
    --white:#ffffff;
  }
  html,body{margin:0;padding:0;width:1200px;height:800px;overflow:hidden;background:var(--page);}
  body{position:relative;font-family:'Poppins',sans-serif;}
  .card{position:absolute;width:560px;height:320px;border-radius:18px;overflow:hidden;
        box-shadow:0 10px 28px rgba(0,0,0,.22);}
  .card svg.art{position:absolute;inset:0;width:560px;height:320px;display:block;}
  .card-back{left:20px;top:240px;}
  .card-front{left:620px;top:240px;}

  .wordmark{position:absolute;color:var(--white);font-weight:600;text-transform:uppercase;
            letter-spacing:.04em;line-height:1.15;margin:0;}
  .card-back .wordmark{left:0;right:0;top:128px;text-align:center;font-size:24px;}
  .card-front .wordmark{left:34px;top:118px;width:200px;font-size:15px;}

  .person{position:absolute;left:286px;top:60px;color:var(--white);margin:0;}
  .person-name{font-size:25px;font-weight:700;letter-spacing:.01em;line-height:1.1;margin:0;}
  .person-role{font-size:15px;font-weight:400;letter-spacing:.03em;margin:2px 0 0;}

  .contact{position:absolute;color:var(--white);font-size:14px;font-weight:300;
           letter-spacing:.04em;line-height:22px;white-space:nowrap;}
</style>
</head>
<body>

<!-- Back of card -->
<section class="card card-back" aria-label="Business card back">
  <svg class="art" viewBox="0 0 560 320" aria-hidden="false">
    <defs>
      <linearGradient id="backShade" x1="0" y1="1" x2="1" y2="0">
        <stop offset="0" stop-color="#060606"/>
        <stop offset="1" stop-color="#2a2a2a"/>
      </linearGradient>
    </defs>
    <rect width="560" height="320" fill="url(#backShade)"/>
    <rect x="330" y="0" width="230" height="120" fill="#2f2f2f" opacity=".35"
          role="img" aria-label="Faint hexagon network pattern"/>
    <rect x="0" y="210" width="200" height="110" fill="#2f2f2f" opacity=".25"
          role="img" aria-label="Faint hexagon network pattern"/>
  </svg>
  <p class="wordmark">Kestrel Roofing &amp; Restoration</p>
</section>

<!-- Front of card -->
<section class="card card-front" aria-label="Business card front">
  <svg class="art" viewBox="0 0 560 320">
    <defs>
      <linearGradient id="frontShade" x1="0" y1="1" x2="1" y2="0">
        <stop offset="0" stop-color="#1e1e1e"/>
        <stop offset="1" stop-color="#333333"/>
      </linearGradient>
    </defs>
    <rect width="560" height="320" fill="var(--ink-dark)"/>
    <rect x="0" y="0" width="300" height="320" fill="url(#frontShade)"
          role="img" aria-label="Subtle hexagon network pattern on dark background"/>
    <!-- left accent bar -->
    <polygon points="44,60 54,66 14,250 2,256" fill="var(--sky)"/>
    <!-- light panel -->
    <polygon points="290,0 560,0 560,320 230,320" fill="var(--sky-pale)"/>
    <!-- name band -->
    <polygon points="280,48 290,52 560,52 560,122 256,122" fill="var(--sky)"/>
    <!-- contact stripes -->
    <g class="stripes">
      <polygon points="247,165 560,165 560,187 243,187" fill="var(--sky)"/>
      <polygon points="247,165 252,158 258,165" fill="var(--fold)"/>
      <polygon points="240,200 560,200 560,222 236,222" fill="var(--sky)"/>
      <polygon points="240,200 245,193 251,200" fill="var(--fold)"/>
      <polygon points="234,235 560,235 560,257 230,257" fill="var(--sky)"/>
      <polygon points="234,235 239,228 245,235" fill="var(--fold)"/>
      <polygon points="227,270 560,270 560,292 223,292" fill="var(--sky)"/>
      <polygon points="227,270 232,263 238,270" fill="var(--fold)"/>
    </g>
    <!-- icons -->
    <g class="icons" fill="none" stroke="var(--sky)" stroke-width="1.4" stroke-linecap="round" stroke-linejoin="round">
      <circle cx="262" cy="176" r="9" fill="var(--white)" stroke="none"/>
      <path d="M258.5 172c0 5 3 8 7.5 8l1-2-2-1.2-1 1c-1.5-.6-2.6-1.8-3.2-3.3l1-1-1.2-2z"/>
      <circle cx="255" cy="211" r="9" fill="var(--white)" stroke="none"/>
      <path d="M255 216s-4-4-4-6.5a4 4 0 0 1 8 0c0 2.5-4 6.5-4 6.5z"/>
      <circle cx="255" cy="209.5" r="1.2"/>
      <circle cx="249" cy="246" r="9" fill="var(--white)" stroke="none"/>
      <rect x="244.5" y="242.5" width="9" height="7" rx="1"/>
      <path d="M244.5 243l4.5 3.5 4.5-3.5"/>
      <circle cx="242" cy="281" r="9" fill="var(--white)" stroke="none"/>
      <circle cx="242" cy="281" r="4.8"/>
      <path d="M237.2 281h9.6M242 276.2c-2 2.8-2 6.8 0 9.6M242 276.2c2 2.8 2 6.8 0 9.6"/>
    </g>
  </svg>

  <p class="wordmark">Kestrel Roofing &amp; Restoration</p>

  <div class="person">
    <h1 class="person-name">YOUR NAME</h1>
    <p class="person-role">DESIGNATION</p>
  </div>

  <span class="contact" style="left:279px;top:165px;">+00123456789</span>
  <span class="contact" style="left:272px;top:200px;">your location here</span>
  <span class="contact" style="left:266px;top:235px;">your address here</span>
  <span class="contact" style="left:259px;top:270px;">your website here</span>
</section>

</body>
</html>
```